IT Company based on Biology Business Needs a Business Card Design

We need a business card design for a new company called 'Lumen CELL'. We develop the machine learning solutions especially focused on deep learning algorithms for biology industry. Our initial product is a vision detection on biological images to help doctors diagnose the symptoms. We would like to see designs that use the color green.

Industry/Entity Type

Business

```html
<!DOCTYPE html>
<html lang="en">
<head>
<meta charset="utf-8">
<title>Lumen CELL – Business Card</title>
<link href="https://fonts.googleapis.com/css2?family=Open+Sans:ital,wght@0,400;0,600;0,700;1,700&display=swap" rel="stylesheet">
<style>
  :root {
    --bg: #b4b9c6;
    --leaf: #7dc242;
    --forest: #0e8a44;
    --paper: #ffffff;
    --ink-light: #ffffff;
  }
  * { margin: 0; padding: 0; box-sizing: border-box; }
  html, body {
    width: 1200px; height: 1000px; overflow: hidden;
    background: var(--bg);
    font-family: "Open Sans", sans-serif;
  }
  .stage { position: relative; width: 1200px; height: 1000px; }

  .card { position: absolute; width: 840px; height: 478px; overflow: hidden; }

  /* Back side */
  .card-back { left: 305px; top: 488px; background: var(--forest); }
  .card-back .rule {
    position: absolute; top: 236px; height: 4px; background: var(--paper);
  }
  .card-back .rule-left { left: 0; width: 253px; }
  .card-back .rule-right { left: 586px; width: 254px; }
  .card-back .brand {
    position: absolute; left: 253px; width: 333px; top: 208px;
    display: flex; align-items: center; justify-content: center; gap: 12px;
    color: var(--paper); font-weight: 600; font-size: 34px; letter-spacing: -0.5px;
  }
  .card-back .brand-dot { width: 16px; height: 16px; border-radius: 50%; background: var(--paper); }

  /* Front side */
  .card-front { left: 52px; top: 70px; width: 838px; background: var(--leaf); }
  .card-front .corner { position: absolute; inset: 0; }
  .card-front .brand {
    position: absolute; left: 645px; top: 74px;
    display: flex; align-items: center; gap: 8px;
    color: var(--leaf); font-weight: 600; font-size: 21px; letter-spacing: -0.3px;
  }
  .card-front .brand-dot { width: 12px; height: 12px; border-radius: 50%; background: var(--leaf); }

  .person { position: absolute; left: 58px; top: 94px; color: var(--ink-light); }
  .person-name { font-weight: 700; font-size: 37px; line-height: 1.1; }
  .person-role { font-weight: 700; font-style: italic; font-size: 29px; line-height: 1.2; }

  .contacts { position: absolute; left: 58px; top: 236px; list-style: none; color: var(--ink-light); font-size: 21.5px; }
  .contacts li { display: flex; align-items: flex-start; gap: 20px; line-height: 28px; margin-bottom: 4.5px; }
  .contacts .icon { width: 25px; height: 28px; flex: none; fill: var(--ink-light); }

  .website { position: absolute; right: 61px; top: 396px; color: var(--ink-light); font-size: 21.5px; }
</style>
</head>
<body>
<main class="stage">

  <section class="card card-back" aria-label="Card back">
    <div class="rule rule-left"></div>
    <div class="brand"><span class="brand-dot"></span>LUMEN CELL</div>
    <div class="rule rule-right"></div>
  </section>

  <section class="card card-front" aria-label="Card front">
    <svg class="corner" width="838" height="478" viewBox="0 0 838 478" aria-hidden="true">
      <polygon points="440,0 838,0 838,288" fill="var(--paper)"/>
      <line x1="447" y1="-3" x2="842" y2="288" stroke="var(--forest)" stroke-width="7"/>
    </svg>

    <div class="brand"><span class="brand-dot"></span>LUMEN CELL</div>

    <div class="person">
      <h1 class="person-name">Mara Quill</h1>
      <p class="person-role">Researcher</p>
    </div>

    <ul class="contacts">
      <li>
        <svg class="icon" viewBox="0 0 25 28"><path d="M1 9h23v12H1z M1 9l11.5 7L24 9" fill="var(--paper)" stroke="var(--leaf)" stroke-width="1.2"/></svg>
        maraquill@lumencell.com
      </li>
      <li>
        <svg class="icon" viewBox="0 0 25 28"><path d="M6 3h12v23H6z M8 6v16h8V6z" fill-rule="evenodd"/></svg>
        555.210.4812
      </li>
      <li>
        <svg class="icon" viewBox="0 0 25 28"><path d="M7 4h9v6H7z M2 11h22v14H2z M4 14h4v3H4z" fill-rule="evenodd"/></svg>
        555.210.4890
      </li>
      <li>
        <svg class="icon" viewBox="0 0 25 28"><path d="M2 12h10v16H2z M12 17h10v11H12z M4 15h2v2H4z M8 15h2v2H8z M4 20h2v2H4z M8 20h2v2H8z M15 20h2v2h-2z M18 20h2v2h-2z" fill-rule="evenodd"/></svg>
        <span>Elm Court No. 12<br>Bristol, U.K.</span>
      </li>
    </ul>

    <p class="website">www.lumencell.com</p>
  </section>

</main>
</body>
</html>
```